HTML Web layout / data visualization for an information software application

We have a product used by patent analysts to allow them examine information stored in patents - particularly those patents that include biological sequences like DNA, RNA, and protein.

When the user opens up a particular patent, they currently see a very poorly organized wall of text, presenting fields of data to them in unorganized ways. We have attached screenshots of the current interface.

The project is to redesign that layout so that the same information is presented in a way which is brings important data to the the eyes of the user, categorizes data appropriately, and is visually appealing. We have proposed logical categorizations of data in the document called "Fields documentation."

The deliverable should be an HTML5 file that renders one or more of the examples of records we've provided in your new design.

Description of files:

"Examples of records badly displayed": MS Word file that shows three different examples of the records we would like to better visualize.

"screengrab1.tiff" and "screengrab2.tiff": pictures of how these records sit inside of our product. This is presented to give you a sense of screen real estate, our look and feel, and colors. We do not want the whole screen redesigned - just the record display itself.

"Fields documentation": detailed documentation of what each field means. We have tried to group them logically for you, and have also attempted to inform you as to which fields are linked to others.
Updates

Hi all,

Thanks for the designs so far. Unfortunately, nearly every design fails to understand the nature of the project. The problem we have is not about fonts and colors (although those matter). It is about grouping information together and displaying data in a way that provides insight. In the original brief, we say:

The document we have uploaded called "Fields documentation" is the most important document. We sense that very few of you have taken it into account. It provides notes on the nature of the data in the report and gives signs of the ways in which a creative designer might help to arrange the content.

Thanks for your consideration of this project.

TL

Target Market(s)

Patent analysts, heavily educated scientists, Ph.Ds.

Industry/Entity Type

Software

```html
<!DOCTYPE html>
<html lang="en">
<head>
<meta charset="utf-8">
<title>SeqVista – Full aln results of workflow BRAF IP</title>
<link rel="stylesheet" href="https://fonts.googleapis.com/css2?family=Arimo:ital,wght@0,400;0,700;1,400&display=swap">
<style>
:root{
  --chrome-top:#ececec;
  --chrome-bottom:#d4d4d4;
  --chrome-line:#a8a8a8;
  --chrome-text:#3a3a3a;
  --page-blue:#d6ebf5;
  --band-blue:#c6e4f1;
  --accent:#1a8fc7;
  --ink:#111;
  --muted:#333;
  --link:#1a73b8;
  --white:#fff;
}
*{box-sizing:border-box;margin:0;padding:0}
html,body{width:1200px;height:873px;overflow:hidden;background:var(--white)}
body{position:relative;font-family:"Arimo",Arial,sans-serif;color:var(--ink)}
.abs{position:absolute}

.titlebar{left:0;top:0;width:1200px;height:32px;background:linear-gradient(var(--chrome-top),#dcdcdc);text-align:center;font-size:17px;line-height:32px;color:var(--chrome-text)}
.light{top:9px;width:15px;height:15px;border-radius:50%;background:#cfcfcf;border:1px solid #a9a9a9}
.toolbar{left:0;top:32px;width:1200px;height:38px;background:#dcdcdc}
.navbtns{left:8px;top:4px;width:62px;height:28px;border:1px solid var(--chrome-line);border-radius:5px;background:var(--white)}
.navbtns::after{content:"";position:absolute;left:30px;top:0;width:1px;height:26px;background:var(--chrome-line)}
.urlbar{left:92px;top:4px;width:1100px;height:28px;border:1px solid var(--chrome-line);border-radius:5px;background:var(--white);font-size:17px;line-height:26px;padding-left:50px;color:var(--ink)}
.urlbar .sitemark{position:absolute;left:28px;top:6px;width:14px;height:14px;border-radius:50%;background:var(--accent)}
.urlbar .plus{position:absolute;left:8px;top:0;color:#666}
.bookmarks{left:0;top:70px;width:1200px;height:38px;background:linear-gradient(#d9d9d9,var(--chrome-bottom));border-bottom:1px solid var(--chrome-line);font-size:16px;line-height:38px;color:var(--chrome-text);white-space:nowrap;padding-left:126px}
.bookmarks span{margin-right:22px}
.bookmarks .icons{position:absolute;left:10px;top:0;color:#555;letter-spacing:10px}

.tabstrip{left:0;top:108px;width:1200px;height:65px;background:var(--page-blue)}
.tab{top:136px;height:37px;border:1px solid #b9c9d2;border-bottom:none;background:#eef4f7;font-size:16px;line-height:36px;text-align:center;color:var(--ink)}
.tab.is-active{background:var(--white);height:38px}

.record-band{left:40px;top:194px;width:1120px;height:74px;background:var(--band-blue)}
.band-hint{left:661px;top:177px;font-size:12px;font-style:italic;color:var(--muted);white-space:nowrap}
.meta{font-size:16px;line-height:19px}
.meta dt{position:absolute;left:0;font-weight:700}
.meta dd{position:absolute;left:103px}

.timeline-line{left:440px;top:239px;width:711px;height:5px;background:#111}
.tick{width:2px;height:14px;top:233px;background:#111}
.dot{width:18px;height:18px;top:232px;border-radius:50%;background:var(--accent)}
.year{top:248px;font-size:17px;color:var(--ink)}
.event{font-size:12px;line-height:14px;text-align:center;color:var(--ink)}

.nav-rail{left:191px;top:310px;width:2px;height:385px;background:var(--accent)}
.nav-item{right:1026px;font-size:16px;color:var(--ink);text-align:right;white-space:nowrap}
.nav-item.is-current{font-weight:700}
.nav-dot{left:188px;width:8px;height:8px;border-radius:50%;background:var(--accent)}
.nav-current-mark{left:183px;width:18px;height:18px;border:3px solid var(--accent);border-radius:50%;background:var(--white)}

.record-title{left:277px;top:308px;width:740px;font-size:16px;line-height:22px;font-weight:700;letter-spacing:.2px}
.field-label{left:277px;font-size:17px;font-weight:700}
.field-value{left:474px;font-size:17px}
.field-value a,.view-link{color:var(--link);text-decoration:underline}
.claim{left:277px;top:577px;width:762px;font-size:16px;line-height:19px;color:var(--ink)}
.view-link{left:277px;top:711px;font-size:16px}
</style>
</head>
<body>

<div class="abs titlebar">SeqVista – Full aln results of workflow BRAF IP</div>
<div class="abs light" style="left:10px"></div>
<div class="abs light" style="left:32px"></div>
<div class="abs light" style="left:54px"></div>

<div class="abs toolbar">
  <div class="abs navbtns"></div>
  <div class="abs urlbar"><span class="plus">+</span><span class="sitemark"></span>https://my.seqvista.example/query?do=gqresult&amp;db=wf:2178462.resdb&amp;is_workspace_recognized=1&amp;</div>
</div>

<div class="abs bookmarks">
  <span class="icons">∞ ▢ ▦</span>
  <span>Cadence Line ▾</span><span>News (85) ▾</span><span>Grants ▾</span><span>Web Favorites ▾</span><span>Orchard</span><span>.Mesa</span><span>Riverbuy</span><span>Bidhall</span><span>Hollo!</span><span>Orchard (32) ▾</span>
</div>

<div class="abs tabstrip"></div>
<div class="abs tab" style="left:14px;width:104px">Alignment</div>
<div class="abs tab is-active" style="left:124px;width:184px">Subject Annotation</div>
<div class="abs tab" style="left:314px;width:173px">Subject Sequence</div>
<div class="abs tab" style="left:493px;width:160px">Query Sequence</div>

<div class="abs record-band"></div>
<div class="abs band-hint">Mouse over blue dots to get exact date</div>

<dl class="abs meta" style="left:58px;top:203px;width:360px;height:60px">
  <dt style="top:0">PN:</dt><dd style="top:0">EP2021499</dd>
  <dt style="top:19px">Assignee:</dt><dd style="top:19px">Redwood Institute</dd>
  <dt style="top:38px">Family:</dt><dd style="top:38px">EP2021499</dd>
</dl>

<div class="abs timeline-line"></div>
<div class="abs tick" style="left:551px"></div>
<div class="abs tick" style="left:662px"></div>
<div class="abs tick" style="left:771px"></div>
<div class="abs tick" style="left:882px"></div>
<div class="abs tick" style="left:991px"></div>
<div class="abs dot" style="left:506px"></div>
<div class="abs dot" style="left:615px"></div>
<div class="abs dot" style="left:889px"></div>
<div class="abs dot" style="left:920px"></div>
<div class="abs dot" style="left:1052px"></div>

<div class="abs event" style="left:480px;top:201px;width:70px">Earliest<br>priority</div>
<div class="abs event" style="left:590px;top:201px;width:70px">Patent<br>filing</div>
<div class="abs event" style="left:770px;top:201px;width:70px">Earliest<br>publication</div>
<div class="abs event" style="left:855px;top:201px;width:80px">Publication<br>date</div>
<div class="abs event" style="left:938px;top:203px;width:50px">Entry<br>date</div>
<div class="abs event" style="left:1025px;top:201px;width:75px">PCT<br>publication</div>
<svg class="abs" style="left:0;top:0" width="1200" height="260" aria-hidden="true">
  <line x1="840" y1="229" x2="893" y2="236" stroke="#111" stroke-width="1"/>
</svg>

<div class="abs year" style="left:423px">2005</div>
<div class="abs year" style="left:533px">2006</div>
<div class="abs year" style="left:642px">2007</div>
<div class="abs year" style="left:752px">2008</div>
<div class="abs year" style="left:863px">2009</div>
<div class="abs year" style="left:972px">2010</div>
<div class="abs year" style="left:1078px">2011</div>

<nav>
  <div class="abs nav-rail"></div>
  <div class="abs nav-item" style="top:323px">Invention</div>
  <div class="abs nav-dot" style="top:329px"></div>
  <div class="abs nav-item" style="top:377px">Identifiers</div>
  <div class="abs nav-dot" style="top:383px"></div>
  <div class="abs nav-item" style="top:430px">Status &amp; priority</div>
  <div class="abs nav-dot" style="top:436px"></div>
  <div class="abs nav-item is-current" style="top:484px">Sequence</div>
  <div class="abs nav-current-mark" style="top:484px"></div>
  <div class="abs nav-item" style="top:537px">Claims</div>
  <div class="abs nav-dot" style="top:543px"></div>
  <div class="abs nav-item" style="top:590px">Miscellaneous</div>
  <div class="abs nav-dot" style="top:596px"></div>
</nav>

<h1 class="abs record-title">FUNCTIONAL ARRAYS FOR HIGH THROUGHPUT CHARACTERIZATION OF GENE EXPRESSION REGULATORY ELEMENTS</h1>

<div class="abs field-label" style="top:383px">SEQ ID NO</div>
<div class="abs field-value" style="top:383px">17040&nbsp;&nbsp;&nbsp;<a>View sequence</a></div>
<div class="abs field-label" style="top:424px">Identifier</div>
<div class="abs field-value" style="top:424px">EP2021499-17040</div>
<div class="abs field-label" style="top:465px">Organism</div>
<div class="abs field-value" style="top:465px">Homo sapiens (Taxonomy ID 9606)</div>
<div class="abs field-label" style="top:506px">Sequence length</div>
<div class="abs field-value" style="top:506px">16,455 nucleotides</div>
<div class="abs field-label" style="top:547px">Location in Patent</div>
<div class="abs field-value" style="top:547px">Claim 1</div>

<p class="abs claim">1. An inhibitory nucleic acid that specifically binds, or is complementary to, an RNA that is known to bind to Polycomb repressive complex 2 (PRC2), optionally an RNA of <b>SEQ ID NO: 17040</b>, or an RNA of any of Tables 1-8 or an RNA of any of SEQ ID NOS: 1 to 193,049, for use in the treatment of disease, wherein the treatment involves modulating expression of a gene targeted by the RNA, wherein the inhibitory nucleic acid is between 5 and 40 bases in length, and wherein the inhibitory nucleic acid is formulated as a sterile composition.</p>

<a class="abs view-link">View all claims</a>

</body>
</html>
```